Brightwave Youth Academy is to provide global summer programs in the United States through which students from the US and China share experiences, intensive learning, and each other’s cultures. The program seeks to more fully prepare both the US and Chinese students for their college education and future careers in this interdependent world. Chinese students are individually paired with US Students where they will reside US students' home for the period of the program.

Current website: Brightwave Youth Academy

Need to support both English and Chinese with different font.
Updates

Project Deadline Extended
Reason: Because of Thanksgiving Holidays.

Dear Designers,

In order to generate the best design, I uploaded some photos from our global summer program. Please check:

http://brightwaveyouthacademy.org/photos/

Doreen

My company Logo just added to the project.

Sorry for the late update.

Project Deadline Extended
Reason: Due to Thanksgiving holiday, I don't have enough time to provide feedback to all the designers. Doreen

Project Deadline Extended
Reason: Holiday season. Need more time for designer and myself.

Target Market(s)

Grade K to 12 students and their parents to sign up the global summer program. Majority audience are from China.

Industry/Entity Type

College

Font styles to use
Sans Serif

Colors
3277b5

Requirements
Must have
• You may check my current website for the summer program content
www.brightwaveyouthacademy.org
Check these two clips to see what service we provided.
http://www.vidplexo.com/watch?v=9kR3mq41bTz&feature=vidplexo.be
https://www.vidplexo.com/watch?v=W7d2HN5p8oJ

Company Logo are included in the attachment.

Some photos from summer program: http://brightwaveyouthacademy.org/photos/
The website should show the students one to one relationship.
The website should show homestay part.

I want Photo Slider on each page to share the fun activities.

Each program will be provide a video clip as a summery.

The website should support font of both English and Chinese. I like to see both Chinese and English on the same page instead of switch back and forth. I can add Chinese part later if you leave the room.

Nice to have
• I have a lot of paired pictures. I am wondering if I can use collage of photos as the background.

The design should be playful and fun!

```html
<!DOCTYPE html>
<html lang="en">
<head>
<meta charset="utf-8">
<title>Brightwave Youth Academy</title>
<link rel="stylesheet" href="https://fonts.googleapis.com/css2?family=Arimo:wght@400;700&display=swap">
<style>
:root{
  --stage:#e6e9ed;
  --navy:#10264a;
  --navy-deep:#0b1c38;
  --blue:#3277b5;
  --blue-dark:#174e8c;
  --card-top:#2a6cb0;
  --card-bottom:#0f3b70;
  --text:#3c3f44;
  --muted:#7b8088;
  --rule:#dfe3e8;
  --white:#ffffff;
  --photo-a:#8c7a5e;
  --photo-b:#c9a070;
  --sky-a:#7aa6d8;
  --sky-b:#4d7a3a;
}
*{box-sizing:border-box;margin:0;padding:0}
html,body{width:1200px;height:660px;overflow:hidden}
body{background:var(--stage);font-family:"Arimo",Arial,sans-serif;color:var(--text);position:relative}
.page{position:absolute;left:360px;top:8px;width:480px;height:644px;background:var(--white);overflow:hidden;box-shadow:0 2px 10px rgba(0,0,0,.15)}
.masthead{position:absolute;left:0;top:0;width:480px;height:190px;background:var(--navy)}
.brand{position:absolute;left:48px;top:14px;display:flex;align-items:center;gap:5px;color:var(--white);font-size:9px;font-weight:400;white-space:nowrap}
.brand-dot{width:12px;height:12px;border-radius:50%;background:var(--white);flex:none}
.nav{position:absolute;left:206px;top:12px;display:flex;background:var(--blue-dark);height:16px}
.nav a{color:var(--white);font-size:6px;text-decoration:none;padding:0 6px;line-height:16px;position:relative;white-space:nowrap}
.nav a.active{background:var(--blue)}
.nav .login{padding-left:14px}
.nav .login::before{content:"";position:absolute;left:5px;top:5px;width:6px;height:6px;background:#e8b93a;border-radius:1px}
.dropdown{position:absolute;left:262px;top:28px;width:70px;background:var(--blue);z-index:5}
.dropdown span{display:block;font-size:5px;color:var(--white);padding:3px 5px;border-bottom:1px solid rgba(255,255,255,.2);white-space:nowrap}
.hero{position:absolute;left:48px;top:38px;width:384px;height:138px;border:3px solid var(--white);background:linear-gradient(180deg,#b8a98e 0%,var(--photo-a) 45%,var(--photo-b) 100%)}
.slider-dots{position:absolute;right:10px;bottom:34px;display:flex;gap:3px}
.slider-dots i{width:6px;height:6px;border-radius:50%;background:var(--white);opacity:.85}
.programs{position:absolute;left:64px;top:168px;width:352px;display:flex;gap:4px;z-index:3}
.program{flex:1;height:52px;padding:4px 6px;background:linear-gradient(180deg,var(--card-top),var(--card-bottom));border-radius:3px;color:var(--white);overflow:hidden}
.program h3{font-size:8px;font-weight:700;margin-bottom:2px;white-space:nowrap}
.program p{font-size:4.5px;line-height:1.35}
.program .more{display:block;text-align:right;font-size:4.5px;font-weight:700}
.content{position:absolute;left:48px;top:230px;width:384px;display:flex;gap:14px}
.main{width:246px}
.sidebar{width:124px}
.welcome h1{font-size:9px;font-weight:400;color:var(--navy)}
.welcome h1 b{font-weight:700}
.welcome .tagline{font-size:6px;color:var(--blue);margin:1px 0 4px}
.welcome .banner{height:36px;background:linear-gradient(180deg,var(--sky-a) 0%,#a9c6e6 55%,var(--sky-b) 100%)}
.body-copy{font-size:4.5px;line-height:1.45;color:var(--muted);margin-top:4px}
.read{display:block;text-align:right;font-size:4.5px;color:var(--blue);font-weight:700;margin-top:1px}
.post{border-top:1px solid var(--rule);margin-top:6px;padding-top:6px;position:relative}
.post h2{font-size:8px;font-weight:400;color:var(--navy);line-height:1.2;width:210px}
.post .meta{font-size:4.5px;color:var(--blue);margin:2px 0 4px}
.post .row{display:flex;gap:5px}
.post .thumb{width:62px;height:30px;flex:none}
.post .thumb.meeting{background:linear-gradient(180deg,#3b2a24,#7a5a46)}
.post .thumb.tennis{background:linear-gradient(180deg,#5a3b2c,#a0674a)}
.post .row p{font-size:4.5px;line-height:1.45;color:var(--muted)}
.date{position:absolute;right:0;top:8px;width:16px;height:14px;background:#f1f2f4;border:1px solid var(--rule);font-size:6px;text-align:center;line-height:12px;font-weight:700;color:var(--text)}
.continue{display:block;text-align:right;font-size:4.5px;color:var(--blue);margin-top:2px}
.sidebar h4{font-size:7px;font-weight:400;color:var(--navy)}
.sidebar .hint{font-size:5px;color:var(--blue);margin:1px 0 4px}
.search{display:flex;gap:2px}
.search span{flex:1;height:8px;border:1px solid var(--rule)}
.search b{font-size:4.5px;color:var(--white);background:var(--navy);padding:0 6px;line-height:8px}
.tabs{display:flex;margin-top:8px}
.tabs span{font-size:5px;font-weight:700;padding:3px 6px;background:var(--blue);color:var(--white);margin-right:1px}
.tabs span.on{background:var(--white);color:var(--navy);border:1px solid var(--rule);border-bottom:none}
.tab-list{border:1px solid var(--rule);padding:2px 4px}
.tab-list li{list-style:none;font-size:4.5px;color:var(--blue);padding:2px 0;border-bottom:1px dotted var(--rule)}
.popular{margin-top:8px}
.popular h4{font-size:8px}
.pop-item{display:flex;gap:4px;margin-top:4px}
.pop-item i{width:14px;height:14px;background:linear-gradient(180deg,#6f8aa8,#b59674);flex:none}
.pop-item p{font-size:4.5px;line-height:1.4;color:var(--muted)}
.pop-item p em{font-style:normal;color:var(--blue)}
.pager{display:flex;justify-content:flex-end;gap:2px;margin-top:4px}
.pager b{width:7px;height:7px;background:var(--navy);color:var(--white);font-size:5px;line-height:7px;text-align:center}
.footer{position:absolute;left:0;top:552px;width:480px;height:92px;background:var(--navy);padding:10px 48px 0;display:flex;gap:18px}
.foot-col h5{font-size:4.5px;color:var(--white);text-transform:uppercase;margin-bottom:4px;font-weight:400}
.foot-col li{list-style:none;font-size:4px;color:#aebbd0;text-transform:uppercase;line-height:1.6}
.album{display:grid;grid-template-columns:repeat(3,20px);gap:3px}
.album i{height:14px;border:1px solid #2b416a;background:linear-gradient(180deg,#b48a5c,#5a4532)}
.album i.gray{background:linear-gradient(180deg,#cfcfcf,#6b6b6b)}
.foot-bar{position:absolute;left:48px;bottom:6px;width:384px;display:flex;justify-content:space-between;font-size:4px;color:#aebbd0}
</style>
</head>
<body>
<div class="page">
  <header class="masthead">
    <div class="brand"><span class="brand-dot"></span>Brightwave Youth Academy</div>
    <nav class="nav">
      <a>Home</a><a>About</a><a class="active">Programs</a><a>Blog</a><a>Events</a><a>Contact</a><a class="login">Login</a>
    </nav>
    <div class="dropdown">
      <span>Harlow Summer Program</span><span>Lakeside Summer Camp</span><span>Whole Year Program</span><span>Homestay Families</span>
    </div>
    <div class="hero" role="img" aria-label="Group photo of US and Chinese students from the summer program standing together in a school hall">
      <div class="slider-dots"><i></i><i></i><i></i><i></i><i></i><i></i></div>
    </div>
  </header>

  <section class="programs">
    <div class="program"><h3>Harlow Summer Program</h3><p>America's top high schools, but also the world's, only a school setting where Lantern Institute School of Chinese culture has a special feeling.</p><span class="more">Read More</span></div>
    <div class="program"><h3>Lakeside Summer Camp</h3><p>Most American children spend an unforgettable summer vacation! The team would like to participate in outdoor summer camp activities.</p><span class="more">Read More</span></div>
    <div class="program"><h3>Whole Year Program</h3><p>We partner with schools, one in America and one in China, so that the students can do projects together, learning, living and having fun under teachers' guidance.</p><span class="more">Read More</span></div>
  </section>

  <div class="content">
    <main class="main">
      <section class="welcome">
        <h1>Welcome to <b>Brightwave Youth Academy</b></h1>
        <p class="tagline">Nurture Global Citizens and Global Leaders</p>
        <div class="banner" role="img" aria-label="Students jumping together on a lawn in front of a city skyline"></div>
        <p class="body-copy">Brightwave Youth Academy is to help American students and Chinese students to break the barriers between the two different cultures, experiences and education backgrounds by providing a global summer program in the U.S. American students and Chinese students one to one paired, home stay in US families, intensive learning and culture adventure activities, and get them fully prepared for their college education and career development in this interdependent world.</p>
        <span class="read">Read More</span>
      </section>
      <article class="post">
        <h2>Chicago Mayor Dalton Reeve and Beijing four students in a cordial conversation</h2>
        <p class="meta">By NEWS SITE in : Interview , Date: February 2nd 2013</p>
        <span class="date">21</span>
        <div class="row">
          <div class="thumb meeting" role="img" aria-label="Mayor meeting four students in an office"></div>
          <p>Lorem ipsum dolor sit amet, consectetur adipiscing elit, sed do eiusmod tempor incididunt ut labore et dolore magna aliqua. Ut enim ad minim veniam, quis nostrud exercitation. Lorem ipsum dolor sit amet, consectetur adipiscing elit.</p>
        </div>
        <span class="continue">Continue Reading</span>
      </article>
      <article class="post">
        <h2>Who is playing the best tennis?</h2>
        <p class="meta">By NEWS SITE in : Interview , Date: February 10th 2013</p>
        <span class="date">02</span>
        <div class="row">
          <div class="thumb tennis" role="img" aria-label="Students playing tennis on an indoor court"></div>
          <p>Lorem ipsum dolor sit amet, consectetur adipiscing elit, sed do eiusmod tempor incididunt ut labore et dolore magna aliqua. Ut enim ad minim veniam, quis nostrud exercitation. Lorem ipsum dolor sit amet, consectetur adipiscing elit.</p>
        </div>
        <span class="continue">Continue Reading</span>
      </article>
    </main>

    <aside class="sidebar">
      <h4>Sidebar content</h4>
      <p class="hint">Insert whatever you want here</p>
      <div class="search"><span></span><b>SEARCH</b></div>
      <div class="tabs"><span class="on">Sports</span><span>Science</span><span>Literature</span></div>
      <ul class="tab-list">
        <li>Cheerleading Cheerleading</li><li>Gymnastics</li><li>Do-It-All Sports Camp</li><li>One World Together</li><li>Tennis Camp</li><li>Community Teen Camp</li>
      </ul>
      <section class="popular">
        <h4>Popular posts</h4>
        <div class="pop-item"><i role="img" aria-label="Post thumbnail"></i><p>Lorem ipsum dolor sit Amet<br><em>21 Comments</em></p></div>
        <div class="pop-item"><i role="img" aria-label="Post thumbnail"></i><p>Lorem ipsum dolor sit Amet<br><em>15 Comments</em></p></div>
        <div class="pop-item"><i role="img" aria-label="Post thumbnail"></i><p>Lorem ipsum dolor sit Amet<br><em>14 Comments</em></p></div>
        <div class="pop-item"><i role="img" aria-label="Post thumbnail"></i><p>Lorem ipsum dolor sit Amet<br><em>21 Comments</em></p></div>
        <div class="pager"><b>&lsaquo;</b><b>&rsaquo;</b></div>
      </section>
    </aside>
  </div>

  <footer class="footer">
    <div class="foot-col"><h5>Alliances</h5><ul><li>Alliance name one</li><li>Alliance name two</li><li>Alliance name three</li><li>Alliance name four</li></ul></div>
    <div class="foot-col"><h5>Support</h5><ul><li>Online support</li><li>Telephone sales</li><li>Workshops</li><li>Online support</li><li>Telephone sales</li><li>Workshops</li></ul></div>
    <div class="foot-col"><h5>Departments</h5><ul><li>Biology</li><li>Science</li><li>IT</li><li>Geography</li><li>Science</li><li>Business</li></ul></div>
    <div class="foot-col"><h5>Photo Album</h5>
      <div class="album" role="img" aria-label="Grid of small program photos">
        <i></i><i class="gray"></i><i class="gray"></i><i></i><i></i><i class="gray"></i>
      </div>
    </div>
    <div class="foot-bar"><span>HOME | ABOUT | NEWS | GALLERY | EVENTS | CONTACT</span><span>&copy; 2013 BRIGHTWAVE YOUTH ACADEMY</span></div>
  </footer>
</div>
</body>
</html>
```